Real Estate Entrepreneur needs a business card

I am a real estate entrepreneur, I buy houses for investment purposes, I act as a real estate agent representing buyers and sellers in residential home transactions, I am a contractor that does a wide range of home repairs and construction. I'd like a design that can stick with me through the years as my business grows and morphs to fit any niche I decide to pursue as markets change.

Target Market(s)

Anyone with interest that may be related to real estate.

Industry/Entity Type

Real Estate

Contact Information for Business Card

A card that stands out and doesn't put me in any one box. My business will evolve over time and I need a card that can stay relevant.

Colors

Designer to choose colors to be used in the design.

Requirements
Must have
• Character
Nice to have
• I'm open
Should not have
• Cliche houses and hammers

```html
<!DOCTYPE html>
<html lang="en">
<head>
<meta charset="utf-8">
<title>Reed Hollow — Business Card</title>
<link href="https://fonts.googleapis.com/css2?family=Work+Sans:wght@400;500;600&display=swap" rel="stylesheet">
<style>
  :root {
    --page-bg: #161616;
    --card-bg: #1d1d1d;
    --card-sheen: #2a2a2a;
    --ink: #ffffff;
    --ink-soft: #d9d9d9;
  }
  * { margin: 0; padding: 0; box-sizing: border-box; }
  html, body {
    width: 1200px;
    height: 900px;
    overflow: hidden;
    background: var(--page-bg);
    font-family: "Work Sans", sans-serif;
  }
  .sheet {
    width: 1200px;
    height: 900px;
    display: flex;
    flex-direction: column;
    align-items: center;
    justify-content: center;
    gap: 40px;
  }
  .card {
    width: 630px;
    height: 360px;
    background: linear-gradient(135deg, var(--card-bg) 0%, var(--card-bg) 55%, var(--card-sheen) 85%, var(--card-bg) 100%);
    color: var(--ink);
    position: relative;
    box-shadow: 0 12px 30px rgba(0, 0, 0, 0.5);
  }
  .card-front {
    display: flex;
    align-items: center;
    justify-content: center;
  }
  .brand-name {
    font-weight: 600;
    font-size: 46px;
    letter-spacing: 0.12em;
    text-transform: uppercase;
  }
  .card-back .identity {
    position: absolute;
    top: 130px;
    left: 0;
    right: 0;
    text-align: center;
  }
  .person-name {
    font-weight: 500;
    font-size: 30px;
    letter-spacing: 0.1em;
    text-transform: uppercase;
  }
  .person-role {
    font-size: 15px;
    letter-spacing: 0.1em;
    color: var(--ink-soft);
    margin-top: -2px;
  }
  .divider {
    width: 84px;
    height: 1px;
    background: var(--ink-soft);
    margin: 10px auto 0;
  }
  .contact-line {
    position: absolute;
    bottom: 34px;
    left: 0;
    right: 0;
    text-align: center;
    font-size: 14.5px;
    letter-spacing: 0.08em;
  }
</style>
</head>
<body>
  <main class="sheet">
    <section class="card card-front">
      <h1 class="brand-name">Reed Hollow</h1>
    </section>
    <section class="card card-back">
      <div class="identity">
        <h2 class="person-name">Reed Hollow</h2>
        <p class="person-role">Director</p>
        <div class="divider"></div>
      </div>
      <p class="contact-line">P : (03) 5550 1842 | E : info@reedhollow.com | W : www.reedhollow.com</p>
    </section>
  </main>
</body>
</html>
```